Travel Group 'Lydgate Group' needs a new business card design

Lydgate Group is a diverse business specialising in bespoke, tailor made holidays to suit all budgets and we are specialists in planning exciting day/short trips to suit all markets. Our target market is very varied going from the corporate client and as well as people in the community who simply want to experience something special.
We are looking for a card design that will encourage people to look at our websites and social media platforms and to see for themselves the different facets to our business. It is essential that the card has social media icons for Facebook, Twitter and Instagram. We are looking for a card with a blank background with no pictures and for the front side to have the attached Lydgate logo. The card should have similar colour scheme to the attached Lydgate logo.
The card must have the following information on one side:
Maud Penrose
Business Development Manager
maudpenrose@lydgatevoyages.example
Lydgate Group, 87 Quarry Lane
Kilwinning, Ayrshire, Scotland KA19 4TN
+44 (0)1294 730182
And then the card must have the following on the second side:
(Lydgate logo)
(social media icons)
www.lydgatevoyages.example
www.lydgateoutings.example
Target Market(s)
Our target market is very varied going from the corporate client and as well as people in the community who simply want to experience something special.
Industry/Entity Type
Business
Contact Information for Business Card
Maud Penrose
+44 (0)1294 730182
(Lydgate logo)
(social media icons)
www.lydgatevoyages.example
www.lydgateoutings.example
Requirements
Must have
- It is essential that the card has social media icons for Facebook, Twitter & Instagram.
Should not have
- Should not have any images other than Lydgate logo.

```html
<!DOCTYPE html>
<html lang="en">
<head>
<meta charset="utf-8">
<title>Lydgate Group – Business Card</title>
<link rel="stylesheet" href="https://fonts.googleapis.com/css2?family=Bebas+Neue&family=Open+Sans:wght@400;600;700&display=swap">
<style>
  :root {
    --card-navy: #2a2463;
    --glow-magenta: #a81c7f;
    --accent-pink: #d9258f;
    --text-white: #ffffff;
    --page-bg: #e9e7ee;
  }
  * { box-sizing: border-box; margin: 0; padding: 0; }
  html, body {
    width: 1200px;
    height: 1000px;
    overflow: hidden;
    background: var(--page-bg);
    font-family: "Open Sans", Arial, sans-serif;
  }
  .stage { position: relative; width: 1200px; height: 1000px; }
  .card {
    position: absolute;
    left: 266px;
    width: 666px;
    height: 397px;
    background: var(--card-navy);
    color: var(--text-white);
    overflow: hidden;
  }
  .card--front {
    top: 74px;
    background:
      radial-gradient(circle at 48% 48%, var(--glow-magenta) 0%, rgba(130, 30, 120, 0.75) 18%, rgba(42, 36, 99, 0) 48%),
      var(--card-navy);
  }
  .card--back { top: 534px; }

  .brand-name {
    position: absolute;
    left: 60px; right: 0;
    top: 212px;
    text-align: center;
    font-weight: 700;
    font-size: 42px;
    line-height: 52px;
    letter-spacing: 3px;
    color: var(--text-white);
  }
  .social-row {
    position: absolute;
    left: 0; right: 0;
    top: 319px;
    display: flex;
    justify-content: center;
    gap: 6px;
  }
  .social-dot {
    width: 18px; height: 18px;
    border-radius: 50%;
    background: var(--text-white);
  }
  .web-links {
    position: absolute;
    left: 0; right: 0;
    top: 349px;
    text-align: center;
    font-size: 15px;
    letter-spacing: 0.2px;
  }
  .web-links .sep { margin: 0 6px; }

  .identity {
    position: absolute;
    right: 372px;
    top: 166px;
    text-align: right;
  }
  .identity__name {
    font-family: "Bebas Neue", Impact, sans-serif;
    font-size: 36px;
    line-height: 36px;
    font-weight: 400;
    color: var(--accent-pink);
    letter-spacing: 0.5px;
  }
  .identity__role { font-size: 15px; margin-top: 2px; }
  .divider {
    position: absolute;
    left: 318px;
    top: 170px;
    width: 2px;
    height: 50px;
    background: var(--accent-pink);
  }
  .contact {
    position: absolute;
    left: 343px;
    top: 172px;
    font-size: 15px;
    line-height: 26px;
  }
  .contact__line { display: flex; align-items: center; gap: 7px; }
  .contact__icon { width: 14px; height: 12px; fill: var(--accent-pink); }
  .address {
    position: absolute;
    left: 0; right: 0;
    top: 346px;
    display: flex;
    justify-content: center;
    align-items: center;
    gap: 6px;
    font-size: 15.5px;
  }
  .address__pin { width: 13px; height: 18px; fill: var(--accent-pink); }
  .address__company { font-weight: 600; color: var(--accent-pink); }
</style>
</head>
<body>
<main class="stage">
  <section class="card card--front" aria-label="Card front">
    <div class="brand-name">LYDGATE</div>
    <div class="social-row" role="img" aria-label="Social media profile icons">
      <span class="social-dot" aria-hidden="true"></span>
      <span class="social-dot" aria-hidden="true"></span>
      <span class="social-dot" aria-hidden="true"></span>
    </div>
    <p class="web-links">www.lydgatevoyages.example<span class="sep">|</span>www.lydgateoutings.example</p>
  </section>

  <section class="card card--back" aria-label="Card back">
    <div class="identity">
      <h1 class="identity__name">Maud Penrose</h1>
      <p class="identity__role">Business Development</p>
    </div>
    <span class="divider"></span>
    <div class="contact">
      <p class="contact__line">
        <svg class="contact__icon" viewBox="0 0 14 12" aria-hidden="true"><path d="M1 3.5C1 2 3 1 7 1s6 1 6 2.5V5h-3V3.8C9 3.5 5 3.5 4 3.8V5H1zM3 6h8l2 4.5H1z"/></svg>
        <span>+44 (0)1294 730182</span>
      </p>
      <p class="contact__line">
        <svg class="contact__icon" viewBox="0 0 14 12" aria-hidden="true"><path d="M1 2h12v8H1zM1.8 2.8v.6L7 6.8l5.2-3.4v-.6z" fill-rule="evenodd"/></svg>
        <span>maudpenrose@lydgatevoyages.example</span>
      </p>
    </div>
    <p class="address">
      <svg class="address__pin" viewBox="0 0 13 18" aria-hidden="true"><path d="M6.5 0A6.5 6.5 0 0 0 0 6.5C0 11 6.5 18 6.5 18S13 11 13 6.5A6.5 6.5 0 0 0 6.5 0zm0 9A2.5 2.5 0 1 1 6.5 4a2.5 2.5 0 0 1 0 5z"/></svg>
      <span><span class="address__company">Lydgate Group</span> 87 Quarry Lane Kilwinning, Ayrshire, Scotland KA19 4TN</span>
    </p>
  </section>
</main>
</body>
</html>
```